Flyer design for new conveyancing business

A flyer to email to real estate agents for referrals for conveyancing work.
Business name "Stonebridge Conveyancing"
Must give a very professional image. Preference is to use images of water etc.
must also contain the following details
Phone: 40912647
admin@stonebridgehomes.com.au
"For all your conveyancing needs from contract to completion"

Target Market(s)

people buying real estate

Industry/Entity Type

Real Estate

Font styles to use
Sans Serif

Colors
33b8a4
33a6d7
86cfc7
85cae6
0556a4

Requirements
Must have
• contact details
• clear text
Should not have
• be too busy

```html
<!DOCTYPE html>
<html lang="en">
<head>
<meta charset="utf-8">
<title>Stonebridge Conveyancing – Flyer</title>
<link href="https://fonts.googleapis.com/css2?family=Source+Sans+3:ital,wght@0,300;0,400;1,300&display=swap" rel="stylesheet">
<style>
  :root {
    --deep-blue: #0556a4;
    --mid-blue: #33a6d7;
    --pale-blue: #85cae6;
    --text-blue: #1e6aa8;
    --white: #ffffff;
  }
  html, body {
    margin: 0;
    padding: 0;
    overflow: hidden;
    background: var(--white);
  }
  .flyer {
    position: relative;
    width: 784px;
    height: 1200px;
    overflow: hidden;
    font-family: "Source Sans 3", sans-serif;
    background: linear-gradient(180deg,
      #1c63b0 0px,
      #3f86c6 110px,
      #a9cdea 210px,
      var(--white) 280px,
      var(--white) 800px,
      #e3f1fa 870px,
      #b3daf0 990px,
      var(--mid-blue) 1110px,
      #2f95d0 1200px);
  }
  .brand-name {
    position: absolute;
    left: 46px;
    top: 84px;
    margin: 0;
    font-weight: 300;
    font-size: 62px;
    line-height: 70px;
    letter-spacing: 0.3px;
    color: var(--white);
  }
  .water-splash {
    position: absolute;
    left: 0;
    top: 290px;
    width: 784px;
    height: 210px;
    background: linear-gradient(180deg,
      rgba(133, 202, 230, 0) 0%,
      rgba(51, 166, 215, 0.55) 45%,
      rgba(5, 86, 164, 0.35) 70%,
      rgba(133, 202, 230, 0) 100%);
  }
  .intro {
    position: absolute;
    left: 136px;
    top: 564px;
    width: 630px;
    margin: 0;
    font-weight: 300;
    font-size: 30px;
    line-height: 42px;
    color: var(--text-blue);
  }
  .tagline {
    position: absolute;
    left: 136px;
    top: 900px;
    margin: 0;
    font-weight: 300;
    font-size: 30px;
    line-height: 42px;
    color: var(--text-blue);
  }
  .slogan {
    position: absolute;
    right: 48px;
    top: 978px;
    margin: 0;
    text-align: right;
    font-weight: 300;
    font-style: italic;
    font-size: 27px;
    line-height: 39px;
    color: var(--white);
  }
  .contact {
    position: absolute;
    right: 48px;
    margin: 0;
    display: flex;
    align-items: center;
    gap: 12px;
    font-weight: 300;
    font-size: 30px;
    line-height: 40px;
    color: var(--white);
  }
  .contact-phone { top: 1070px; }
  .contact-email { top: 1120px; }
  .contact svg { display: block; }
</style>
</head>
<body>
  <main class="flyer">
    <h1 class="brand-name">stonebridge conveyancing</h1>

    <div class="water-splash" role="img" aria-label="Photograph of a splashing wave of clear blue water across the flyer"></div>

    <p class="intro">Buying or selling your home, land or<br>investment property requires professionalism<br>and transparency.<br>At stonebridge conveyancing, we have the<br>expertise to assist you in any conveyance<br>and at an attractive price.<br>Let us be part of your team.</p>

    <p class="tagline">– clearly, the right choice.</p>

    <p class="slogan">"For all your conveyancing needs from<br>contract to completion"</p>

    <p class="contact contact-phone">
      <svg width="30" height="30" viewBox="0 0 24 24" aria-hidden="true"><path fill="#ffffff" d="M6.6 10.8a15.1 15.1 0 0 0 6.6 6.6l2.2-2.2c.3-.3.7-.4 1-.2 1.1.4 2.3.6 3.6.6.6 0 1 .4 1 1V20c0 .6-.4 1-1 1C10.6 21 3 13.4 3 4c0-.6.4-1 1-1h3.5c.6 0 1 .4 1 1 0 1.3.2 2.5.6 3.6.1.3 0 .7-.2 1z"/></svg>
      <span>4091-2647</span>
    </p>
    <p class="contact contact-email">
      <svg width="38" height="28" viewBox="0 0 36 26" aria-hidden="true"><rect x="1" y="1" width="34" height="24" fill="#ffffff"/><path d="M1 1 L18 15 L35 1" fill="none" stroke="#33a6d7" stroke-width="2"/></svg>
      <span>admin@stonebridgehomes.com.au</span>
    </p>
  </main>
</body>
</html>
```